We would like to create a flyer with our logo I have attached and would like you to add the BrindlecoteBID logo at the bottom.
I would like the flyer to have a urban vintage style to it.
Please add:
Email: Info@brindlecotebid.co.uk
Twitter account: @Brindlecotebid
Facebook account: The Parade Retro and Collectors Fair
Address: The Parade, Brindlecote, W19 4QX
Dates: Saturday 27 september 2014
Saturday 25 October 2014
Saturday 29 November 2014.
Please hight light the dates and the location.

Target Market(s)

Every one.

Font styles to use
Other font styles liked:
• Market Deco

Requirements
Must have
• My project should be eye catching.
• Dates and location should be clear.
• Please use this font: ‘Market Deco’
• Please source images which will suit the logo and style of layout.
Nice to have
• Colours which will contrast with the logo.
• Colour of logo is: purple is P95 -16c
• The layout on the word doc I like.

```html
<!DOCTYPE html>
<html lang="en">
<head>
<meta charset="utf-8">
<title>BrindlecoteBID – The Parade Retro and Collectors Fair flyer</title>
<link rel="stylesheet" href="https://fonts.googleapis.com/css2?family=Arvo:wght@400;700&family=Limelight&family=Playfair+Display:wght@700&family=Oswald:wght@400&display=swap">
<style>
  :root {
    --backdrop: #e9e6e2;
    --plum-deep: #5e2250;
    --plum-mid: #7c3a6a;
    --plum-light: #955283;
    --ink-white: #f6f0f4;
    --ribbon-yellow: #f2de2b;
    --ribbon-shade: #c9b31c;
    --ribbon-fold: #a8931a;
    --date-ink: #4a4548;
    --mint: #e7f3e7;
    --mint-edge: #6cb54a;
    --lilac: #c48bbd;
    --lilac-edge: #9b5d93;
    --butter: #f4ee92;
    --butter-edge: #e6c52b;
    --tag-bg: #3b1940;
    --tag-ink: #efe4ee;
    --ornament: rgba(246, 240, 244, 0.28);
  }
  * { box-sizing: border-box; margin: 0; padding: 0; }
  html, body { width: 1200px; height: 900px; overflow: hidden; background: var(--backdrop); }
  .canvas { position: relative; width: 1200px; height: 900px; }
  .flyer {
    position: absolute; left: 290px; top: 20px; width: 620px; height: 860px;
    background: radial-gradient(ellipse at 50% 42%, var(--plum-light) 0%, var(--plum-mid) 45%, var(--plum-deep) 100%);
    box-shadow: 0 6px 22px rgba(0,0,0,0.25);
    overflow: hidden;
  }
  .flyer-frame {
    position: absolute; inset: 20px; border: 2px solid var(--ink-white); opacity: 0.9;
  }
  .ornament { position: absolute; background: var(--ornament); border-radius: 40px; }
  .ornament--crest-top { left: 215px; top: 62px; width: 190px; height: 34px; }
  .ornament--crest-bottom { left: 225px; top: 190px; width: 170px; height: 32px; }
  .ornament--scroll-left { left: 72px; top: 420px; width: 58px; height: 150px; }
  .ornament--scroll-right { left: 488px; top: 362px; width: 58px; height: 140px; }
  .ornament--corner { width: 44px; height: 44px; border-radius: 50%; }
  .ornament--corner.tl { left: 10px; top: 10px; }
  .ornament--corner.tr { right: 10px; top: 10px; }
  .ornament--corner.bl { left: 10px; bottom: 10px; }
  .ornament--corner.br { right: 10px; bottom: 10px; }

  .location {
    position: absolute; left: 0; right: 0; top: 112px; text-align: center;
    font-family: "Arvo", serif; font-weight: 700; font-size: 27px; line-height: 36px;
    color: var(--ink-white); letter-spacing: 0.5px;
  }

  .day-ribbon { position: absolute; left: 60px; top: 282px; width: 500px; height: 100px; }
  .day-ribbon svg { position: absolute; inset: 0; }
  .day-ribbon__label {
    position: absolute; left: 0; right: 0; top: 24px; text-align: center;
    font-family: "Limelight", sans-serif; font-size: 40px; letter-spacing: 3px;
    color: var(--date-ink);
  }

  .dates { position: absolute; left: 0; top: 396px; width: 620px; }
  .date-chip {
    position: absolute; height: 44px; padding: 0 16px;
    font-family: "Playfair Display", serif; font-weight: 700; font-size: 29px; line-height: 46px;
    letter-spacing: 1px; white-space: nowrap;
  }
  .date-chip--sep { left: 186px; top: 0; background: var(--mint); color: var(--date-ink); box-shadow: 5px 5px 0 var(--mint-edge); }
  .date-chip--oct { left: 208px; top: 54px; background: var(--lilac); color: var(--ink-white); box-shadow: 5px 5px 0 var(--lilac-edge); }
  .date-chip--nov { left: 196px; top: 108px; background: var(--butter); color: var(--date-ink); box-shadow: 5px 5px 0 var(--butter-edge); }

  .contacts { position: absolute; right: 48px; top: 592px; width: 340px; height: 120px; }
  .contact-row { position: absolute; right: 0; display: flex; align-items: center; gap: 10px; }
  .contact-row--email { top: 0; }
  .contact-row--page { top: 42px; right: 0; }
  .contact-row--social { top: 80px; }
  .contact-icon { width: 26px; height: 26px; border-radius: 50%; background: var(--ink-white); display: flex; align-items: center; justify-content: center; flex: none; }
  .contact-tag {
    background: var(--tag-bg); color: var(--tag-ink); border: 1px solid rgba(239,228,238,0.35);
    font-family: "Oswald", sans-serif; font-size: 12px; letter-spacing: 1px; text-transform: uppercase;
    padding: 3px 8px; white-space: nowrap;
  }
  .contact-amp { font-family: "Arvo", serif; color: var(--ornament); font-size: 18px; }

  .brand { position: absolute; left: 80px; top: 730px; display: flex; align-items: center; gap: 12px; }
  .brand__mark { width: 34px; height: 34px; background: var(--ink-white); }
  .brand__name { font-family: "Arvo", serif; font-weight: 700; font-size: 30px; color: var(--ink-white); }
</style>
</head>
<body>
<main class="canvas">
  <article class="flyer">
    <div class="flyer-frame"></div>
    <div class="ornament ornament--corner tl" role="img" aria-label="Corner flourish ornament"></div>
    <div class="ornament ornament--corner tr" role="img" aria-label="Corner flourish ornament"></div>
    <div class="ornament ornament--corner bl" role="img" aria-label="Corner flourish ornament"></div>
    <div class="ornament ornament--corner br" role="img" aria-label="Corner flourish ornament"></div>

    <div class="ornament ornament--crest-top" role="img" aria-label="Vintage scroll flourish above the address"></div>
    <p class="location">The Parade,<br>Brindlecote, W19 4QX</p>
    <div class="ornament ornament--crest-bottom" role="img" aria-label="Vintage scroll flourish below the address"></div>

    <div class="day-ribbon">
      <svg viewBox="0 0 500 100" width="500" height="100" aria-hidden="true">
        <polygon points="0,44 70,44 70,92 0,92 22,68" fill="var(--ribbon-shade)"/>
        <polygon points="430,2 500,2 478,26 500,50 430,50" fill="var(--ribbon-shade)"/>
        <polygon points="50,74 70,74 70,92" fill="var(--ribbon-fold)"/>
        <polygon points="430,30 450,30 430,14" fill="var(--ribbon-fold)"/>
        <polygon points="50,22 450,12 450,64 50,74" fill="var(--ribbon-yellow)"/>
      </svg>
      <div class="day-ribbon__label">SATURDAY 2014</div>
    </div>

    <div class="ornament ornament--scroll-left" role="img" aria-label="Curling leaf scroll ornament"></div>
    <div class="ornament ornament--scroll-right" role="img" aria-label="Curling leaf scroll ornament"></div>

    <div class="dates">
      <div class="date-chip date-chip--sep">27 SEPTEMBER</div>
      <div class="date-chip date-chip--oct">25 OCTOBER</div>
      <div class="date-chip date-chip--nov">29 NOVEMBER</div>
    </div>

    <div class="contacts">
      <div class="contact-row contact-row--email">
        <span class="contact-icon">
          <svg width="16" height="12" viewBox="0 0 16 12" aria-hidden="true">
            <rect x="0.5" y="0.5" width="15" height="11" fill="none" stroke="var(--plum-mid)" stroke-width="1.4"/>
            <polyline points="0.5,0.5 8,7 15.5,0.5" fill="none" stroke="var(--plum-mid)" stroke-width="1.4"/>
          </svg>
        </span>
        <span class="contact-tag">Info@brindlecotebid.co.uk</span>
      </div>
      <div class="contact-row contact-row--page">
        <span class="contact-icon"></span>
        <span class="contact-tag">The Parade Retro</span>
        <span class="contact-amp">&amp;</span>
        <span class="contact-tag">Collectors Fair</span>
      </div>
      <div class="contact-row contact-row--social">
        <span class="contact-icon"></span>
        <span class="contact-tag">@Brindlecotebid</span>
      </div>
    </div>

    <div class="brand">
      <span class="brand__mark"></span>
      <span class="brand__name">BrindlecoteBID</span>
    </div>
  </article>
</main>
</body>
</html>
```